Letterhead Design Project

We have just had a letterhead desinged on word which is pretty basic and boring. We are looking for a professional and modern letterhead to suit our business for letters and quotes. We are an irrigation business that looks at providing a garden enhancement package. We do instore sales, internet sales and design and installation. We would like the colours to be similar to what is on our website. www.kestonirrigation.com.au
Industry/Entity Type
Internet
Requirements
Must have
- We would like to include:
find us on chatterly and blipzo,
member of plovant stores,
Catchphrase: "The Garden Enhancement Specialist"
Verified Greenline Dealer Logo
phone, fax, email & website

```html
<!DOCTYPE html>
<html lang="en">
<head>
<meta charset="utf-8">
<title>Keston Irrigation Supplies – Letterhead</title>
<link rel="stylesheet" href="https://fonts.googleapis.com/css2?family=Open+Sans:wght@400;600;700&display=swap">
<style>
  :root {
    --backdrop: #333333;
    --paper: #ffffff;
    --band-top: #6ab4e8;
    --band-bottom: #3f6fc4;
    --strip: #1c1c1c;
    --brand-blue: #2a8fd0;
    --tagline: #5aa3dd;
    --ink: #3a3f4a;
    --member-green: #1f8a3a;
    --badge: #2e9a48;
    --rule: #d8d8d8;
  }
  * { box-sizing: border-box; margin: 0; padding: 0; }
  html, body { width: 1200px; height: 900px; overflow: hidden; }
  body { background: var(--backdrop); font-family: "Open Sans", Arial, sans-serif; position: relative; }

  .letterhead {
    position: absolute; left: 317px; top: 40px; width: 576px; height: 820px;
    background: var(--paper); overflow: hidden;
  }
  .band { position: absolute; left: 0; width: 100%; background: linear-gradient(180deg, var(--band-top), var(--band-bottom)); }
  .band--top { top: 0; height: 51px; }
  .band--bottom { bottom: 0; height: 31px; background: linear-gradient(180deg, var(--band-bottom), var(--band-top)); }
  .strip { position: absolute; left: 0; width: 100%; background: var(--strip); }
  .strip--top { top: 51px; height: 6px; }
  .strip--bottom { bottom: 31px; height: 6px; }

  .header-shape, .footer-shape { position: absolute; }
  .header-shape { left: 0; top: 57px; width: 280px; height: 56px; }
  .footer-shape { right: 0; bottom: 37px; width: 340px; height: 56px; }

  .brand {
    position: absolute; left: 44px; top: 73px; width: 205px;
    display: flex; align-items: center; gap: 7px; white-space: nowrap;
    font-weight: 600; font-size: 14px; line-height: 20px; color: var(--brand-blue);
  }
  .brand__dot { flex: none; width: 10px; height: 10px; border-radius: 50%; background: var(--brand-blue); }

  .tagline {
    position: absolute; left: 280px; top: 72px; white-space: nowrap;
    font-weight: 700; font-size: 13px; line-height: 18px; color: var(--tagline);
  }
  .membership { position: absolute; right: 14px; top: 93px; width: 90px; text-align: right; }
  .membership__label { font-size: 9px; font-style: italic; font-weight: 600; color: var(--member-green); margin-right: 16px; }
  .membership__badge { display: block; margin: 2px 0 0 auto; width: 80px; height: 26px; border-radius: 4px; background: var(--badge); }

  .contact {
    position: absolute; left: 21px; top: 739px; font-style: normal;
    font-size: 9.5px; line-height: 13px; color: var(--ink);
  }
  .social { position: absolute; left: 276px; top: 742px; display: flex; align-items: center; gap: 8px; }
  .social__icon { width: 38px; height: 32px; border-radius: 4px; background: #3d6fb4; }
  .social__links { font-size: 9px; line-height: 12px; color: var(--ink); white-space: nowrap; }

  .website { position: absolute; left: 24px; bottom: 9px; font-size: 11px; color: #ffffff; }
</style>
</head>
<body>
  <main class="letterhead">
    <div class="band band--top"></div>
    <div class="strip strip--top"></div>

    <svg class="header-shape" viewBox="0 0 280 56" aria-hidden="true">
      <polygon points="0,0 272,0 255,52 0,52" fill="#ffffff"/>
      <polyline points="0,52 255,52 272,0" fill="none" stroke="var(--rule)" stroke-width="2"/>
    </svg>

    <div class="brand"><span class="brand__dot"></span>Keston Irrigation Supplies</div>
    <p class="tagline">THE GARDEN ENHANCEMENT SPECIALIST</p>
    <div class="membership">
      <p class="membership__label">A member of</p>
      <span class="membership__badge" role="img" aria-label="Plovant Stores member badge"></span>
    </div>

    <svg class="footer-shape" viewBox="0 0 340 56" aria-hidden="true">
      <polygon points="18,2 340,2 340,56 0,56" fill="#ffffff"/>
      <polyline points="0,56 18,2 340,2" fill="none" stroke="var(--rule)" stroke-width="2"/>
    </svg>

    <address class="contact">
      Phone: (03) 9000 4417<br>
      Fax: (03) 9000 4418<br>
      Email: sales@kestonirrigation.com.au
    </address>

    <div class="social">
      <span class="social__icon" aria-hidden="true"></span>
      <p class="social__links">
        www.chatterly.com/pages/Keston-Irrigation-Supplies<br>
        www.blipzo.com/#!/KestonIrrigati
      </p>
    </div>

    <div class="strip strip--bottom"></div>
    <div class="band band--bottom"></div>
    <p class="website">www.kestonirrigation.com.au</p>
  </main>
</body>
</html>
```